ORVA MELKANTE - LUXURY RESORT CORVAL HOTEL

We wanna promote the luxury hotel based on marroquian stylish luxury decor, it is still a project but we need to expose it.
Houses will be A frame type houses surrounded by florest and water dumps - please check - odeleite amber heron at google to check localisation
Container luxury houses also will be included heaven blue velvet and green and rose gold are the Color. The sky is the limit.

```html
<!DOCTYPE html>
<html lang="en">
<head>
<meta charset="utf-8">
<title>Orva Melkante – Letterhead</title>
<link rel="stylesheet" href="https://fonts.googleapis.com/css2?family=Poppins:wght@300;400;500;600;700&family=Cinzel:wght@400&display=swap">
<style>
  :root{
    --backdrop:#74909a;
    --paper:#ffffff;
    --ink:#2e2a28;
    --ink-soft:#3a3636;
    --muted:#a7a3ab;
    --gold:#b88a52;
    --gold-dark:#8c6431;
    --band-grey:#545252;
    --band-text:#d9d6d2;
  }
  *{box-sizing:border-box;margin:0;padding:0}
  html,body{width:1200px;height:903px;overflow:hidden;background:var(--backdrop)}
  body{font-family:"Poppins",sans-serif;color:var(--ink)}
  .letterhead{
    position:absolute;left:296px;top:21px;width:608px;height:860px;
    background:var(--paper);box-shadow:0 10px 30px rgba(0,0,0,.25);overflow:hidden;
  }
  .header-rule{position:absolute;left:0;top:0;width:608px;height:120px}
  .brand-name{
    position:absolute;left:40px;top:62px;font-size:20px;font-weight:400;
    letter-spacing:4px;color:var(--gold);white-space:nowrap;
  }
  .letter-date{position:absolute;right:44px;top:108px;font-size:9px;color:var(--ink)}
  .letter-date b{color:var(--gold);font-weight:600}
  .recipient{position:absolute;left:60px;top:150px;font-size:9px;line-height:13px}
  .recipient .recipient-name{color:var(--gold);font-weight:600;font-size:10px}
  .recipient .recipient-role{font-weight:600;text-transform:uppercase}
  .letter-body{position:absolute;left:82px;top:228px;width:470px;font-size:9.5px;line-height:14px}
  .letter-body p{margin-bottom:14px}
  .letter-body .para-light{color:var(--muted)}
  .letter-body .para-dark{color:var(--ink-soft)}
  .signoff{position:absolute;right:48px;top:590px;width:180px;text-align:center}
  .signature-mark{display:block;width:150px;height:44px;margin:0 auto 6px;
    background:linear-gradient(90deg,#f4f2f0,#e6e2de);border-radius:4px}
  .signer-name{font-size:11px;font-weight:600;letter-spacing:.5px}
  .signer-title{font-size:7.5px;letter-spacing:.5px;margin-top:2px}
  .contacts{position:absolute;left:36px;top:690px}
  .contact-row{display:flex;align-items:center;gap:12px;margin-bottom:10px}
  .contact-icon{width:26px;height:26px;border-radius:50%;
    background:radial-gradient(circle at 35% 30%,#d3a86f,var(--gold-dark));
    display:flex;align-items:center;justify-content:center}
  .contact-text{font-size:8.5px;line-height:12px;color:var(--ink)}
  .contact-text b{font-weight:700}
  .footer-band{position:absolute;left:0;top:800px;width:608px;height:40px}
  .footer-address{font-family:"Poppins",sans-serif;font-weight:600;font-size:10px;letter-spacing:1.5px;fill:#fff}
  .footer-tagline{font-family:"Cinzel",serif;font-size:10px;letter-spacing:1.2px;fill:var(--band-text)}
</style>
</head>
<body>
<main class="letterhead">
  <svg class="header-rule" viewBox="0 0 608 120" aria-hidden="true">
    <rect x="266" y="66" width="92" height="7" fill="var(--ink)"/>
    <line x1="358" y1="69.5" x2="608" y2="69.5" stroke="var(--ink)" stroke-width="1.2"/>
  </svg>
  <div class="brand-name">ORVA MELKANTE</div>

  <div class="letter-date"><b>Date:</b> 24-03-2018</div>

  <div class="recipient">
    <div>To</div>
    <div class="recipient-name">Nolan Brisk</div>
    <div class="recipient-role">CEO, Veltram Studio</div>
    <div><b>W:</b> www.veltramstudio.com</div>
  </div>

  <section class="letter-body">
    <p class="para-light">Lorem ipsum dolor sit amet, consectetur adipiscing elit. Pellentesque dictum, ante non ullamcorper convallis, nunc quam blandit metus, ac mollis eros felis a orci. Donec congue, mauris ut pulvinar lobortis, dolor massa feugiat nisi, at tincidunt metus leo vel elit. Proin facilisis semper lobortis. Vivamus augue purus, cursus quis urna non, accumsan pellentesque est. Nulla in iaculis magna, quis aliquet ex. Cras efficitur metus eget purus euismod facilisis. Proin non metus tincidunt, auctor ipsum a, tempor mi.</p>
    <p class="para-dark">Nulla egestas vulputate risus, ut vestibulum diam commodo id. Mauris ornare libero eu erat porttitor ultrices. Proin sed lectus scelerisque ligula bibendum sagittis ac nec leo. Donec ac accumsan diam, et lobortis mauris.</p>
    <p class="para-dark">Nulla congue volutpat nisl ac lobortis. Integer dignissim interdum libero, quis feugiat velit pretium at. Phasellus sit amet libero rutrum, feugiat odio et, tempus purus. Cras ultricies, leo at fringilla sollicitudin, leo sapien placerat enim, a rutrum lorem enim ut tortor. Phasellus magna ante, congue maximus egestas sit amet, venenatis scelerisque felis.</p>
    <p class="para-light">Nulla congue volutpat nisl ac lobortis. Integer dignissim interdum libero, quis feugiat velit pretium at. Phasellus sit amet libero rutrum, feugiat odio et, tempus purus. Cras ultricies, leo at fringilla sollicitudin, leo sapien placerat enim, a rutrum lorem enim ut tortor. Phasellus magna ante, congue maximus egestas sit amet, venenatis scelerisque felis.</p>
  </section>

  <div class="signoff">
    <span class="signature-mark" role="img" aria-label="Handwritten signature of Selin Marovat"></span>
    <div class="signer-name">[ SELIN MAROVAT ]</div>
    <div class="signer-title">FOUNDER</div>
  </div>

  <div class="contacts">
    <div class="contact-row">
      <span class="contact-icon">
        <svg width="13" height="13" viewBox="0 0 24 24" aria-hidden="true"><path d="M6.6 10.8a15 15 0 0 0 6.6 6.6l2.2-2.2a1 1 0 0 1 1-.25 11.4 11.4 0 0 0 3.6.57 1 1 0 0 1 1 1V20a1 1 0 0 1-1 1A17 17 0 0 1 3 4a1 1 0 0 1 1-1h3.5a1 1 0 0 1 1 1c0 1.25.2 2.45.57 3.57a1 1 0 0 1-.25 1z" fill="#fff"/></svg>
      </span>
      <div class="contact-text"><b>T:</b> +20 10 5550 1842<br><b>F:</b> +20 10 5550 1843</div>
    </div>
    <div class="contact-row">
      <span class="contact-icon">
        <svg width="13" height="13" viewBox="0 0 24 24" aria-hidden="true"><rect x="3" y="6" width="18" height="12" rx="1" fill="none" stroke="#fff" stroke-width="2"/><path d="M3 7l9 6 9-6" fill="none" stroke="#fff" stroke-width="2"/></svg>
      </span>
      <div class="contact-text"><b>E:</b> selin.marovat@corvalhotel.com<br><b>W:</b> www.corvalhotel.com</div>
    </div>
    <div class="contact-row">
      <span class="contact-icon">
        <svg width="13" height="13" viewBox="0 0 24 24" aria-hidden="true"><circle cx="12" cy="12" r="9" fill="none" stroke="#fff" stroke-width="2"/><ellipse cx="12" cy="12" rx="4" ry="9" fill="none" stroke="#fff" stroke-width="1.6"/><path d="M3 12h18" stroke="#fff" stroke-width="1.6"/></svg>
      </span>
    </div>
  </div>

  <svg class="footer-band" viewBox="0 0 608 40" aria-hidden="true">
    <polygon points="0,0 325,0 335,20 325,40 0,40" fill="var(--ink)"/>
    <polygon points="325,0 560,0 570,20 560,40 325,40 335,20" fill="var(--band-grey)"/>
    <polygon points="560,0 608,0 608,40 560,40 570,20" fill="var(--ink)"/>
    <text class="footer-address" x="70" y="24">NORTH RIDGE - SALVEN BAY</text>
    <text class="footer-tagline" x="350" y="24">LUXURY RESORT CORVAL HOTEL</text>
  </svg>
</main>
</body>
</html>
```